Maple Leap Movement Retreats 2016 Brochure

Hi there! Maple Leap Movement Retreats (www.MapleLeapMovementRetreats.com) operates overnight dance camps for girls ages 8 - 17 in eight U.S. states. We need a designer to help us create our 2016 brochure.

Most prospective camper families will download the brochure through our website, but some may also request to have a print version sent via mail, so the brochure will need to be print quality.

We'd like the brochure to be similar to our 2015 brochure (attached, both print & web), just with new pictures & correct dates/rates/offers. Also, we recently migrated our website to wordpress, so we'd like the brochure to have a similar look/feel to our new site in terms of fonts, colors, etc.

Using the attached program as a template, I'd love to have designers submit a mock up for our 2016 cover as well as a couple inside pages.

Newer pictures can be accessed online:
Flickr username: marla_quibey / pw: Rosalind5678
Instagram: @leapmlmr

The fonts on our website are "Mountains of Christmas" and "PT Sans". Attached are a couple higher quality versions of our logo as well.

Also, just want to mention that I'm looking to develop a longer-term relationship with a designer - many projects in the pipeline :-)

Thanks!

Harriet
hquorvel@leapmlmr.com

```html
<!DOCTYPE html>
<html lang="en">
<head>
<meta charset="utf-8">
<title>Maple Leap Movement Retreats – 2016 Dates &amp; Rates</title>
<link rel="stylesheet" href="https://fonts.googleapis.com/css2?family=Mountains+of+Christmas:wght@400;700&family=PT+Sans:ital,wght@0,400;0,700&display=swap">
<style>
  :root {
    --magenta: #93336a;
    --magenta-deep: #8a3560;
    --magenta-bright: #a13b76;
    --leaf: #b0d57b;
    --stone: #c5c0bd;
    --rule: #9b9b9b;
    --ink: #1d1d1d;
    --paper: #ffffff;
  }
  * { box-sizing: border-box; margin: 0; padding: 0; }
  html, body { width: 1200px; height: 1099px; overflow: hidden; background: var(--paper); }
  .page { position: relative; width: 1200px; height: 1099px; font-family: "PT Sans", Arial, sans-serif; color: var(--ink); }

  .header-band { position: absolute; left: 0; top: 30px; width: 1200px; height: 163px; background: var(--leaf); }
  .header-block { position: absolute; left: 0; top: 0; width: 958px; height: 168px; background: var(--magenta); }
  .header-title {
    position: absolute; left: 54px; top: 56px;
    font-family: "Mountains of Christmas", cursive;
    font-weight: 700; font-size: 52px; line-height: 1; color: var(--paper);
    letter-spacing: 0.5px;
  }

  table { border-collapse: collapse; table-layout: fixed; position: absolute; }
  td, th { border: 2px solid var(--rule); text-align: center; vertical-align: middle; }

  .schedule { left: 59px; top: 255px; width: 1084px; }
  .schedule col { width: 361px; }
  .camp-name { background: var(--leaf); color: var(--paper); font-weight: 400; font-size: 17px; line-height: 1.3; }
  .camp-name.row-a { height: 49px; }
  .camp-name.row-b { height: 49px; }
  .camp-name.row-c { height: 44px; }
  .sessions { font-size: 18px; font-weight: 700; line-height: 1.35; }
  .sessions.row-a { height: 113px; vertical-align: top; padding-top: 14px; }
  .sessions.row-b { height: 65px; }
  .sessions.row-c { height: 44px; }
  .shade { background: var(--stone); }
  .plain { background: var(--paper); }

  .rates { left: 69px; top: 770px; width: 625px; }
  .rates th { background: var(--leaf); color: var(--paper); font-weight: 400; font-size: 18px; height: 49px; }
  .rates td { height: 49.5px; font-size: 17.5px; }
  .rates .count, .rates .price { font-weight: 700; }
  .rates .early { background: var(--magenta-deep); color: var(--paper); }
  .rates .saving { background: var(--magenta-bright); color: var(--paper); }
  .rates tr.alt .early { background: var(--magenta-bright); }
  .rates tr.alt .saving { background: var(--magenta-deep); }

  .campers-photo { position: absolute; left: 740px; top: 635px; width: 420px; height: 444px; }
</style>
</head>
<body>
<div class="page">
  <div class="header-band"></div>
  <div class="header-block"></div>
  <h1 class="header-title">2016 MLMR Dates &amp; Rates</h1>

  <table class="schedule">
    <colgroup><col><col><col></colgroup>
    <tr>
      <th class="camp-name row-a">SUMMIT Green Mountains<br>Stratton, VT</th>
      <th class="camp-name row-a">SUMMIT Sierra Mountains<br>Squaw Valley, CA</th>
      <th class="camp-name row-a">SUMMIT MID ATLANTIC<br>Baltimore County, MD</th>
    </tr>
    <tr>
      <td class="sessions row-a shade">Session 1: June 26 - July 2<br>Session 2: July 3 - 9<br>Session 3: July 10 - 16<br>Session 4: July 17 - 23</td>
      <td class="sessions row-a plain">Session 1: June 26 - July 2<br>Session 2: July 3 - 9<br>Session 3: July 10 - 16<br>Session 4: July 17 - 23</td>
      <td class="sessions row-a shade">Session 1: July 17 - 23<br>Session 2: July 24 - 30</td>
    </tr>
    <tr>
      <th class="camp-name row-b">SUMMIT Chicago Lake Shore<br>Lake Forest, IL</th>
      <th class="camp-name row-b">SUMMIT BLUE RIDGE MOUNTAINS<br>Asheville, NC</th>
      <th class="camp-name row-b">SUMMIT TRI-STATE<br>Lawrenceville, NJ</th>
    </tr>
    <tr>
      <td class="sessions row-b shade">Session 1: June 19 - 25<br>Session 2: June 26 - July 2</td>
      <td class="sessions row-b plain">Session 1: July 10 - 16</td>
      <td class="sessions row-b shade">1 Session: July 31 - Aug 6</td>
    </tr>
    <tr>
      <th class="camp-name row-c">SUMMIT ROCKY Mountains<br>Winter Park, CO</th>
      <th class="camp-name row-c">SUMMIT CENTRAL LAKES<br>Beaver Dam, WI</th>
      <th class="camp-name row-c"></th>
    </tr>
    <tr>
      <td class="sessions row-c shade">Session 1: June 19 - 25</td>
      <td class="sessions row-c plain">Session 1: July 10 - 16</td>
      <td class="sessions row-c shade"></td>
    </tr>
  </table>

  <table class="rates">
    <colgroup><col style="width:156px"><col style="width:160px"><col style="width:155px"><col style="width:154px"></colgroup>
    <tr><th>SESSIONS</th><th>2016 RATE</th><th>RATE BY 4/18</th><th>SAVINGS</th></tr>
    <tr><td class="count shade">1 Session</td><td class="price shade">$1499</td><td class="early">$1299</td><td class="saving">$200 OFF</td></tr>
    <tr class="alt"><td class="count plain">2 Sessions</td><td class="price plain">$1469 / Session</td><td class="early">$1269 / Session</td><td class="saving">$460 OFF</td></tr>
    <tr><td class="count shade">3 Sessions</td><td class="price shade">$1439 / Session</td><td class="early">$1239 / Session</td><td class="saving">$780 OFF</td></tr>
    <tr class="alt"><td class="count plain">4 Sessions</td><td class="price plain">$1409 / Session</td><td class="early">$1209 / Session</td><td class="saving">$1160 OFF</td></tr>
  </table>

  <svg class="campers-photo" role="img" aria-label="Photo of three young dancers in black tops, green tutus and leg warmers, arms around each other" viewBox="0 0 420 444">
    <defs>
      <radialGradient id="campersTone" cx="50%" cy="45%" r="60%">
        <stop offset="0%" stop-color="#d9b49a"/>
        <stop offset="55%" stop-color="#b7c98e"/>
        <stop offset="100%" stop-color="#ffffff" stop-opacity="0"/>
      </radialGradient>
    </defs>
    <rect width="420" height="444" fill="url(#campersTone)"/>
  </svg>
</div>
</body>
</html>
```